Veltarum

Standard Business Card design.
Sample two-sided design uploaded. White front, Black back.
Would like white shield to be on all black background side.
Willing to look at a couple creative designs, but nothing crazy.
Preference for a classic, confident, strong design.

```html
<!DOCTYPE html>
<html lang="en">
<head>
<meta charset="UTF-8">
<title>Veltarum Business Card</title>
<link href="https://fonts.googleapis.com/css2?family=Orbitron:wght@500;700&family=Roboto:wght@400&display=swap" rel="stylesheet">
<style>
  :root {
    --backdrop: #262626;
    --card: #101010;
    --card-edge: #1c1c1c;
    --emboss: #3b3b3b;
    --ink: #f2f2f2;
    --muted: #b5b5b5;
  }
  * { margin: 0; padding: 0; box-sizing: border-box; }
  html, body { width: 900px; height: 1200px; overflow: hidden; background: var(--backdrop); }
  .stage { position: relative; width: 900px; height: 1200px; background: var(--backdrop); }
  .card {
    position: absolute; left: 135px; width: 630px; height: 360px;
    background: var(--card); border: 1px solid var(--card-edge);
  }
  .card--front { top: 210px; }
  .card--back { top: 600px; }

  .brand-front {
    position: absolute; left: 0; right: 0; top: 150px;
    display: flex; align-items: center; justify-content: center; gap: 22px;
  }
  .brand-mark { width: 44px; height: 44px; background: var(--emboss); }
  .brand-name {
    font-family: "Orbitron", sans-serif; font-weight: 700; font-size: 50px;
    letter-spacing: 6px; color: var(--emboss); line-height: 1;
  }

  .brand-back {
    position: absolute; right: 42px; top: 42px;
    display: flex; align-items: center; gap: 12px;
  }
  .brand-back .brand-mark { width: 22px; height: 22px; background: var(--ink); }
  .brand-back .brand-name { font-size: 22px; letter-spacing: 3px; color: var(--ink); }

  .person { position: absolute; left: 45px; top: 232px; }
  .person-name {
    font-family: "Orbitron", sans-serif; font-weight: 500; font-size: 20px;
    letter-spacing: 2px; color: var(--ink);
  }
  .person-role {
    font-family: "Roboto", sans-serif; font-size: 13px; color: var(--muted); margin-top: 6px;
  }
  .contacts { list-style: none; margin-top: 16px; }
  .contacts li {
    display: flex; align-items: center; gap: 10px; height: 22px;
    font-family: "Roboto", sans-serif; font-size: 13px; color: var(--ink); letter-spacing: 0.5px;
  }
  .contacts svg { width: 13px; height: 13px; fill: var(--ink); flex: none; }
</style>
</head>
<body>
<div class="stage">
  <section class="card card--front">
    <div class="brand-front">
      <span class="brand-mark"></span>
      <span class="brand-name">VELTARUM</span>
    </div>
  </section>

  <section class="card card--back">
    <div class="brand-back">
      <span class="brand-mark"></span>
      <span class="brand-name">VELTARUM</span>
    </div>
    <div class="person">
      <div class="person-name">DANA WHITFORD</div>
      <div class="person-role">Founder</div>
      <ul class="contacts">
        <li>
          <svg viewBox="0 0 24 24"><path d="M6.6 10.8a15.1 15.1 0 0 0 6.6 6.6l2.2-2.2c.3-.3.7-.4 1-.2 1.1.4 2.3.6 3.6.6.6 0 1 .4 1 1V20c0 .6-.4 1-1 1C10.6 21 3 13.4 3 4c0-.6.4-1 1-1h3.5c.6 0 1 .4 1 1 0 1.3.2 2.5.6 3.6.1.3 0 .7-.2 1z"/></svg>
          555-018-2740
        </li>
        <li>
          <svg viewBox="0 0 24 24"><path d="M2 5h20v14H2z M4 7v.5l8 5 8-5V7l-8 5z" fill-rule="evenodd"/></svg>
          info@veltarum.com
        </li>
        <li>
          <svg viewBox="0 0 24 24"><circle cx="12" cy="12" r="10"/></svg>
          www.veltarum.com
        </li>
      </ul>
    </div>
  </section>
</div>
</body>
</html>
```